Cool Simple Design for Baby Product

Our company is Tovarin. We need a package design for our cupboard lock product. We want to appear as caring, warm and close to earth company that aims to improve family life.

Logo is our company logo, colour can be changed if you feel the need for it. Pics 1 and 2 are of the product itself. Pics 3 to 6 are examples of packages and visuals that I do like very much, maybe something along those lines.

Pics 7 and 8 a re just examples of something that I do NOT like. They feel too busy and detailed.

UPDATE: Colourbox1 is the main file that you should work on, colourbox2 is sample of the suppliers default look, so you can see how it looks when it is assembled.

There will be little text, but not much, ALSO there will be text in Germany so please consider this when creating the design. It is not yet finalized what text there will be but something like this:

"Text1: This is English text and there will not be much more than these characters, but also there will be German translation in this same space"

"Text2: Maybe this text too, overall 300 English characters maximum on whole package and that's it"

Industry/Entity Type

Baby

Font styles to use
Decorative
Script

Requirements
Must have
• Simple, soothing, cool, valuable.
Nice to have
• Less is more.
Should not have
• Aggressive with lot of details and too much stuff.

```html
<!DOCTYPE html>
<html lang="en">
<head>
<meta charset="utf-8">
<title>Tovarin cupboard lock mailer box dieline</title>
<link rel="stylesheet" href="https://fonts.googleapis.com/css2?family=Arimo&family=Quicksand:wght@500&family=Great+Vibes&display=swap">
<style>
  :root {
    --paper: #ffffff;
    --board: #fbfae3;
    --cut: #a24f9c;
    --crease: #7cc45c;
    --band: #a3d4ac;
    --band-text: #ffffff;
    --seal-ring: #a3d4ac;
    --seal-text: #c67fc0;
    --tag-frame: #d3a0cc;
    --art-tone: #e3e7a6;
    --dim: #a04f9a;
    --label: #222222;
  }
  html, body { margin: 0; padding: 0; width: 1200px; height: 1200px; overflow: hidden; background: var(--paper); }
  .dieline { display: block; width: 1200px; height: 1200px; }
  .panel { fill: var(--board); stroke: var(--cut); stroke-width: 1.4; }
  .crease { fill: none; stroke: var(--crease); stroke-width: 1.2; stroke-dasharray: 14 6; }
  .band { fill: var(--band); }
  .band-stitch { fill: none; stroke: #fff; stroke-width: 1.2; stroke-dasharray: 6 5; }
  .cutout { fill: #fff; stroke: var(--cut); stroke-width: 1.4; }
  .seal-ring { fill: #fff; stroke: var(--seal-ring); stroke-width: 6; }
  .seal-dots { fill: none; stroke: var(--seal-text); stroke-width: 1; stroke-dasharray: 1.5 3; }
  .brand-name { font-family: "Quicksand", sans-serif; font-weight: 500; font-size: 19px; fill: var(--seal-text); text-anchor: middle; }
  .side-copy { font-family: "Great Vibes", cursive; font-size: 13px; fill: var(--band-text); }
  .dim-line { stroke: var(--dim); stroke-width: 1.3; fill: none; }
  .dim-arrow { fill: var(--dim); }
  .dim-label { font-family: "Arimo", sans-serif; font-size: 22px; fill: var(--label); text-anchor: middle; }
  .tag-frame { fill: #fff; stroke: var(--tag-frame); stroke-width: 10; }
  .tag-art { fill: var(--art-tone); }
  .tag-fold { stroke: var(--crease); stroke-width: 1.3; stroke-dasharray: 10 6; }
</style>
</head>
<body>
<svg class="dieline" viewBox="0 0 1500 1500" xmlns="http://www.w3.org/2000/svg">

  <!-- dimensions -->
  <g class="dimensions">
    <line class="dim-line" x1="221" y1="148" x2="221" y2="308"/>
    <line class="dim-line" x1="1394" y1="145" x2="1394" y2="307"/>
    <line class="dim-line" x1="228" y1="210" x2="1387" y2="210"/>
    <polygon class="dim-arrow" points="221,210 234,205 234,215"/>
    <polygon class="dim-arrow" points="1394,210 1381,205 1381,215"/>
    <text class="dim-label" x="818" y="196">325 mm</text>

    <line class="dim-line" x1="65" y1="274" x2="326" y2="274"/>
    <line class="dim-line" x1="67" y1="1432" x2="328" y2="1432"/>
    <line class="dim-line" x1="157" y1="281" x2="159" y2="1425"/>
    <polygon class="dim-arrow" points="157,274 152,287 162,287"/>
    <polygon class="dim-arrow" points="159,1432 154,1419 164,1419"/>
    <text class="dim-label" x="93" y="895">321 mm</text>
  </g>

  <!-- lid tuck flap -->
  <g class="lid-tuck">
    <path class="panel" d="M543,272 L1077,272 L1077,285 C1160,292 1196,320 1196,358 C1196,392 1175,403 1085,405 L1075,410 L1062,418 L557,418 L543,410 L533,405 C445,403 425,392 425,358 C425,320 460,292 543,285 Z"/>
    <rect class="band" x="425" y="322" width="771" height="53"/>
    <line class="band-stitch" x1="430" y1="328" x2="1190" y2="328"/>
    <line class="band-stitch" x1="430" y1="369" x2="1190" y2="369"/>
    <line class="crease" x1="543" y1="285" x2="543" y2="410"/>
    <line class="crease" x1="1077" y1="285" x2="1077" y2="410"/>
    <g transform="translate(817 347) rotate(180)">
      <circle class="seal-ring" r="45"/>
      <circle class="seal-dots" r="37"/>
      <text class="brand-name" y="7">Tovarin</text>
    </g>
  </g>

  <!-- lid panel with dust flaps -->
  <g class="lid">
    <path class="panel" d="M557,420 L430,468 C425,472 425,478 425,490 L425,700 C425,712 428,720 440,725 L557,777 Z"/>
    <path class="panel" d="M1062,420 L1189,468 C1195,472 1196,478 1196,490 L1196,700 C1196,712 1192,720 1180,725 L1062,777 Z"/>
    <rect class="panel" x="557" y="420" width="505" height="365" stroke="none"/>
    <line class="crease" x1="557" y1="420" x2="1062" y2="420"/>
    <line class="crease" x1="557" y1="420" x2="557" y2="785"/>
    <line class="crease" x1="1062" y1="420" x2="1062" y2="785"/>
    <rect class="cutout" x="692" y="598" width="235" height="10" rx="5"/>
  </g>

  <!-- front wall -->
  <g class="front-wall">
    <path class="panel" d="M543,785 L1083,785 L1083,797 L1200,797 C1210,797 1213,803 1213,812 L1213,905 C1213,914 1208,918 1198,918 L1090,918 L1083,930 L543,930 L535,918 L422,918 C412,918 408,913 408,904 L408,812 C408,803 412,797 422,797 L543,797 Z"/>
    <rect class="band" x="408" y="828" width="805" height="60"/>
    <line class="band-stitch" x1="412" y1="836" x2="1209" y2="836"/>
    <line class="band-stitch" x1="412" y1="880" x2="1209" y2="880"/>
    <line class="crease" x1="543" y1="785" x2="1083" y2="785"/>
    <line class="crease" x1="543" y1="797" x2="543" y2="918"/>
    <line class="crease" x1="1083" y1="797" x2="1083" y2="918"/>
    <g transform="translate(817 858)">
      <circle class="seal-ring" r="48"/>
      <circle class="seal-dots" r="40"/>
      <text class="brand-name" y="7">Tovarin</text>
    </g>
  </g>

  <!-- base with side walls -->
  <g class="base">
    <path class="panel" d="M238,938 L375,938 L375,930 L1245,930 L1245,936 L1382,936 L1382,1050 L1397,1058 L1397,1157 L1382,1165 L1382,1280 L1245,1280 L1245,1287 L375,1287 L375,1280 L238,1280 L238,1167 L223,1160 L223,1058 L238,1052 Z"/>
    <line class="crease" x1="537" y1="930" x2="1083" y2="930"/>
    <line class="crease" x1="537" y1="1287" x2="1083" y2="1287"/>
    <line class="crease" x1="537" y1="930" x2="537" y2="1287"/>
    <line class="crease" x1="1083" y1="930" x2="1083" y2="1287"/>
    <line class="crease" x1="375" y1="938" x2="375" y2="1280"/>
    <line class="crease" x1="393" y1="935" x2="393" y2="1285"/>
    <line class="crease" x1="1227" y1="935" x2="1227" y2="1285"/>
    <line class="crease" x1="1245" y1="936" x2="1245" y2="1280"/>

    <rect class="band" x="437" y="930" width="60" height="357"/>
    <rect class="band" x="423" y="998" width="87" height="222"/>
    <text class="side-copy" transform="translate(448 1205) rotate(-90)">
      <tspan x="0" y="0">This is English text and there will not be much</tspan>
      <tspan x="0" y="22">more than these characters, but also there will be</tspan>
      <tspan x="0" y="44">German translation in this same space</tspan>
    </text>

    <rect class="band" x="1125" y="930" width="60" height="357"/>
    <rect class="band" x="1112" y="998" width="87" height="222"/>
    <text class="side-copy" transform="translate(1175 1015) rotate(90)">
      <tspan x="0" y="0">This is English text and there will not be much</tspan>
      <tspan x="0" y="22">more than these characters, but also there will be</tspan>
      <tspan x="0" y="44">German translation in this same space</tspan>
    </text>

    <rect class="cutout" x="535" y="1055" width="17" height="107"/>
    <rect class="cutout" x="1069" y="1053" width="17" height="109"/>
  </g>

  <!-- back wall -->
  <g class="back-wall">
    <path class="panel" d="M552,1287 L1070,1287 L1070,1297 L1198,1297 C1208,1297 1213,1302 1213,1312 L1213,1405 C1213,1414 1208,1420 1198,1420 L1080,1420 L1070,1432 L552,1432 L542,1420 L422,1420 C412,1420 408,1414 408,1405 L408,1312 C408,1302 412,1297 422,1297 L552,1297 Z"/>
    <line class="crease" x1="552" y1="1297" x2="552" y2="1420"/>
    <line class="crease" x1="1070" y1="1297" x2="1070" y2="1420"/>
    <g transform="translate(810 1360) rotate(180)">
      <circle class="seal-ring" r="48"/>
      <circle class="seal-dots" r="40"/>
      <text class="brand-name" y="7">Tovarin</text>
    </g>
  </g>

  <!-- hang tag -->
  <g class="hang-tag">
    <path class="tag-frame" d="M1258,505 C1270,480 1300,472 1330,484 L1475,508 L1464,835 L1243,835 L1243,668 L1256,660 C1246,620 1243,545 1258,505 Z"/>
    <rect class="tag-art" x="1262" y="505" width="190" height="250" rx="14" role="img" aria-label="Illustration of a baby fitting a cupboard lock, with the word Locked!"/>
    <line class="tag-fold" x1="1240" y1="772" x2="1468" y2="772"/>
  </g>

</svg>
</body>
</html>
```